Executive retreat/workshop flyer for Harbor Pathway

Our company, Harbor Pathway, runs intensive week long residential retreats for executives suffering from burnout syndrome. We have a programme of therapy which will enable clients to get clarity on what they want out of life and how to achieve it.

Our website is www.harborpathway-example.com. The flyer should have a consistent look and feel to the website. The flyer should be suitable for electronic distribution as well as printing.

The copy should read:

What is it all for? (IN BIG BOLD FONT)

We invite you to The Harbor Pathway

Discover a more meaningful way of being in this world and put passion and purpose back into your life.

Our leading experts will guide you through a holistic program of intellectual, physical, emotional, spiritual and financial work.

You will:

- Draw up a vision of how you want to live your life
- Understand negative behavior loops and how to manage them
- Rebalance relationships which have suffered from stress and neglect
- Examine your attitudes towards money through the Quadrafold System
- Access practical advice on how to implement your goals

Please join us in the beautiful Castlereagh Peninsula this August for a life-changing journey.

This is an intensive program custom tailored to your individual needs. We can only take on a very limited number of participants to maintain intimacy and quality of attention. Book early to avoid disappointment.

Details:

date - mon 27 August - sat 1 sept 2012

Venue- kestrelwood Eco retreat, stony ford, Australia, 1 hour from Melbourne

Price- Special launch offer of US$ 13,860 which is a 30% discount off the normal price of US$ 19,800

10% of profits go to charity

All accommodation, food and individual consultations included.

Please email info@harborpathway-example.com or contact Marnie at 6031 2946

Target Market(s)

Senior executives and leaders mostly with a financial background.

Industry/Entity Type

Residential

Requirements
Must have
• The brochure should look clear in electronic and print format. Can use photos which I've attached.
Nice to have
• Should have a warm, serene feel but appear professional and reliable.

```html
<!DOCTYPE html>
<html lang="en">
<head>
<meta charset="utf-8">
<title>Harbor Pathway – Retreat Flyer</title>
<link href="https://fonts.googleapis.com/css2?family=Didact+Gothic&display=swap" rel="stylesheet">
<style>
  :root {
    --page: #ffffff;
    --olive: #a9a67f;
    --olive-dark: #8c8968;
    --olive-light: #c9c7a6;
    --olive-ring: #b8b58e;
    --grass-top: #6f8a4c;
    --grass-bottom: #3f5a2a;
    --plum: #4e1650;
    --plum-mid: #6e2a70;
    --blossom: #b06cb3;
    --ink: #3a3a3a;
    --white: #ffffff;
  }
  * { margin: 0; padding: 0; box-sizing: border-box; }
  html, body {
    width: 868px; height: 1200px; overflow: hidden;
    background: var(--page);
    font-family: "Didact Gothic", "Century Gothic", sans-serif;
  }
  .flyer {
    position: absolute; left: 49px; top: 45px;
    width: 766px; height: 1084px;
    background: var(--page);
    box-shadow: 0 2px 14px rgba(0,0,0,.45);
    overflow: hidden;
  }
  .hero-photo {
    position: absolute; left: 0; top: 0; width: 766px; height: 296px;
    background: linear-gradient(180deg, #9aa58a 0%, var(--grass-top) 22%, var(--grass-bottom) 100%);
  }
  .intro {
    position: absolute; left: 0; top: 296px; width: 766px; height: 236px;
    background: radial-gradient(ellipse at 60% 70%, var(--olive-light) 0%, var(--olive) 45%, var(--olive-dark) 100%);
  }
  .title-band {
    position: absolute; left: 0; top: 296px; width: 766px; height: 46px;
    background: rgba(214,212,180,.55);
    border-bottom: 2px solid var(--olive-ring);
  }
  .headline {
    position: absolute; left: 6px; top: 294px;
    font-size: 46px; color: var(--white); letter-spacing: 1px; line-height: 50px;
    font-weight: 400;
  }
  .invite {
    position: absolute; left: 12px; top: 343px;
    font-size: 27px; color: var(--plum); line-height: 34px;
  }
  .intro-copy {
    position: absolute; left: 12px; top: 393px; width: 620px;
    font-size: 16px; line-height: 20px; color: var(--white);
  }
  .intro-copy p + p { margin-top: 20px; }
  .intro-copy p.wide { width: 745px; }
  .brand-seal {
    position: absolute; left: 565px; top: 261px; width: 194px; height: 194px;
    border-radius: 50%; background: var(--white);
    border: 9px solid var(--olive-ring);
    display: flex; flex-direction: column; align-items: center; justify-content: center;
    color: var(--plum); text-align: center;
  }
  .brand-name { font-size: 19px; line-height: 22px; margin-top: 40px; }
  .brand-url { font-size: 10.5px; margin-top: 6px; }
  .rule-plum { position: absolute; left: 0; top: 530px; width: 766px; height: 4px; background: var(--plum); }
  .outcomes { position: absolute; left: 0; top: 534px; width: 766px; height: 211px; background: var(--white); }
  .outcomes h2 {
    position: absolute; left: 16px; top: 26px;
    font-size: 41px; font-weight: 400; color: var(--olive);
  }
  .outcomes ul {
    position: absolute; left: 14px; top: 93px; list-style: none;
    font-size: 17.5px; line-height: 21.6px; color: var(--plum);
  }
  .rule-olive { position: absolute; left: 0; top: 743px; width: 766px; height: 3px; background: var(--olive-ring); }
  .details {
    position: absolute; left: 0; top: 746px; width: 766px; height: 306px;
    color: var(--white);
  }
  .details-photo {
    position: absolute; inset: 0;
    background: radial-gradient(ellipse at 38% 45%, var(--blossom) 0%, var(--plum-mid) 40%, var(--plum) 100%);
  }
  .details-copy { position: absolute; left: 10px; top: 12px; width: 750px; font-size: 13px; line-height: 16px; }
  .details-copy p + p { margin-top: 16px; }
  .details h3 { font-size: 30px; font-weight: 400; margin-top: 14px; margin-bottom: 8px; }
  .details ul { list-style: none; }
  .details li { line-height: 16px; margin-bottom: 16px; }
  .contact {
    position: absolute; left: 0; top: 1052px; width: 766px; height: 32px;
    border-top: 3px solid var(--blossom);
    text-align: right; padding-right: 12px;
    font-size: 17px; line-height: 28px; color: var(--ink);
  }
</style>
</head>
<body>
  <main class="flyer">
    <div class="hero-photo" role="img" aria-label="Photo of a pale greyhound resting in long green grass"></div>
    <section class="intro">
    </section>
    <div class="title-band"></div>
    <h1 class="headline">WHAT IS IT ALL FOR?</h1>
    <p class="invite">We invite you to The Harbor Pathway</p>
    <div class="intro-copy">
      <p>Discover a more meaningful way of being in this world and put passion and purpose back into your life.</p>
      <p class="wide">Our leading experts will guide you through a holistic program of intellectual, physical, emotional, spiritual and financial work.</p>
    </div>
    <div class="brand-seal">
      <span class="brand-name">The Harbor Pathway</span>
      <span class="brand-url">WWW.HARBORPATHWAY-EXAMPLE.COM</span>
    </div>

    <div class="rule-plum"></div>
    <section class="outcomes">
      <h2>You will:</h2>
      <ul>
        <li>- Draw up a vision of how you want to live your life</li>
        <li>- Understand negative behavior loops and how to manage them</li>
        <li>- Rebalance relationships which have suffered from stress and neglect</li>
        <li>- Examine your attitudes towards money through the Quadrafold System</li>
        <li>- Access practical advice on how to implement your goals</li>
      </ul>
    </section>
    <div class="rule-olive"></div>

    <section class="details">
      <div class="details-photo" role="img" aria-label="Photo of a hand holding a cluster of purple blossoms"></div>
      <div class="details-copy">
        <p>Please join us in the beautiful Castlereagh Peninsula this August for a life-changing journey.</p>
        <p>This is an intensive program custom tailored to your individual needs. We can only take on a very limited number of participants to maintain intimacy and quality of attention. Book early to avoid disappointment.</p>
        <h3>Details:</h3>
        <ul>
          <li>date - mon 27 August - sat 1 sept 2012</li>
          <li>Venue- kestrelwood Eco retreat, stony ford, Australia, 1 hour from Melbourne</li>
          <li>Price- Special launch offer of US$ 13,860 which is a 30% discount off the normal price of US$ 19,800</li>
          <li>10% of profits go to charity</li>
          <li>All accommodation, food and individual consultations included.</li>
        </ul>
      </div>
    </section>

    <footer class="contact">Please email info@harborpathway-example.com or contact Marnie at 6031 2946</footer>
  </main>
</body>
</html>
```